Design a Full Page PDF Brochure "white paper" (Adobe InDesign)

Hello, my business needs a template to create "white papers" for our website. These are the free PDF downloads that you see on websites for lead capture.

The winning entry will need the following seven characteristics:
(1) A consistent color palette (or scheme) and feel of our website and logo (which I've attached). Even thought it is called a "white paper", please use lots of color and make it vibrant.
(2) A cover sheet that fills up the whole page, it also needs to have contact information on it (you can use this for now):

Ferris Oakhurst
48 Lindel Rd
Springfield, USA
414-555-0171
ferris@quabbleton.example
[login to view URL]

It's important that our logo is used as part of the cover page design. Feel free to be creative with this.

(3) The text needs to have different sized subheadings (H1, H2, H3)
(4) I would suggest adding "call outs" to highlight quotes from the text
(5) I would suggest submitting entries with multiple page layouts that can be used
(6) You may use Latin text and stock photos that I will replace. Our website [login to view URL] uses a theme of hiking, mountains, and paths.
(7) The final page needs to also have the contact information on it

To help clarify what I'm looking for, here are some examples of white papers:
[login to view URL]
[login to view URL]
[login to view URL]

The entries need to be in Adobe InDesign. The winner needs to turn over the final InDesign Files along with any supporting files such as in Adobe Illustrator.

Also, please do not contact me outside of Taskory (doing so will disqualify your entries).

Thank you ahead of time for your work.

```html
<!DOCTYPE html>
<html lang="en">
<head>
<meta charset="utf-8">
<title>Alderpine Advisors — White Paper Cover Spread</title>
<link rel="stylesheet" href="https://fonts.googleapis.com/css2?family=Barlow+Semi+Condensed:wght@500;700&family=Roboto:wght@400;500;700&display=swap">
<style>
  :root {
    --backdrop: #e8e8e8;
    --paper: #ffffff;
    --leaf: #8bc34a;
    --leaf-deep: #7ab23c;
    --mist: #ececef;
    --fog-light: #f1f1f3;
    --fog-mid: #b7bcbd;
    --forest: #2a3a34;
    --forest-deep: #1c2824;
    --ink-light: #ffffff;
  }
  * { box-sizing: border-box; margin: 0; padding: 0; }
  html, body { width: 1200px; height: 788px; overflow: hidden; }
  body {
    background: var(--backdrop);
    font-family: "Roboto", Arial, sans-serif;
    position: relative;
  }
  .spread {
    position: absolute;
    left: 180px; top: 97px;
    width: 840px; height: 594px;
    display: flex;
    box-shadow: 0 6px 18px rgba(0,0,0,.12);
  }
  .page {
    position: relative;
    width: 420px; height: 594px;
    background: var(--paper);
    overflow: hidden;
  }

  /* Back cover */
  .back-photo {
    position: absolute; inset: 0;
    background: linear-gradient(180deg, var(--fog-light) 0%, #d9dcdd 35%, var(--fog-mid) 55%, #5b6a64 75%, var(--forest) 88%, var(--forest-deep) 100%);
  }
  .contact-panel {
    position: absolute;
    left: 106px; top: 172px;
    width: 314px; height: 250px;
    background: var(--leaf);
    color: var(--ink-light);
    padding: 26px 0 0 44px;
  }
  .contact { margin-bottom: 9px; font-size: 6.5px; line-height: 1.4; }
  .contact .name {
    font-family: "Barlow Semi Condensed", "Arial Narrow", sans-serif;
    font-weight: 700; font-size: 7.5px; letter-spacing: .04em; text-transform: uppercase;
  }
  .brand {
    display: flex; align-items: center; gap: 5px;
    font-family: "Barlow Semi Condensed", "Arial Narrow", sans-serif;
    font-weight: 700; letter-spacing: .04em; text-transform: uppercase;
  }
  .brand .dot { width: 9px; height: 9px; border-radius: 50%; background: currentColor; }
  .contact-panel .brand {
    position: absolute; left: 50%; bottom: 14px; transform: translateX(-50%);
    font-size: 11px; color: var(--ink-light);
  }

  /* Front cover */
  .front-photo {
    position: absolute; left: 0; top: 0;
    width: 330px; height: 175px;
    background: linear-gradient(180deg, #f4f4f5 0%, #dfe2e2 45%, #a9b1ae 80%, #6f7c76 100%);
  }
  .web-tag {
    position: absolute; right: 88px; top: 12px;
    width: 92px; height: 14px;
    background: var(--leaf);
    color: var(--ink-light);
    font-size: 5.5px; line-height: 14px; text-align: center;
  }
  .mist-panel {
    position: absolute; left: 90px; top: 175px;
    width: 282px; height: 162px;
    background: var(--mist);
  }
  .title-panel {
    position: absolute; left: 0; top: 95px;
    width: 330px; height: 210px;
    background: var(--leaf);
    color: var(--ink-light);
    padding: 46px 0 0 64px;
  }
  .kicker {
    font-family: "Barlow Semi Condensed", "Arial Narrow", sans-serif;
    font-weight: 700; font-size: 19px; line-height: 1; letter-spacing: .01em;
  }
  .headline {
    font-family: "Barlow Semi Condensed", "Arial Narrow", sans-serif;
    font-weight: 700; font-size: 40px; line-height: .92; letter-spacing: .01em;
  }
  .lede {
    position: relative;
    margin-top: 18px;
    width: 200px;
    font-size: 6.5px; line-height: 1.5;
    padding-left: 12px;
  }
  .lede::before {
    content: ""; position: absolute; left: 0; top: 2px; bottom: 2px;
    width: 1px; background: var(--ink-light);
  }
  .page-front .brand {
    position: absolute; left: 50%; top: 395px; transform: translateX(-50%);
    font-size: 13px; color: var(--leaf-deep);
  }
</style>
</head>
<body>
  <main class="spread">
    <section class="page page-back">
      <div class="back-photo" role="img" aria-label="Misty pine forest fading from white fog at the top to dark evergreen trees at the bottom"></div>
      <div class="contact-panel">
        <div class="contact"><p class="name">Wren Halloway</p><p>720.555.0148</p><p>wren.halloway@alderpine.example</p></div>
        <div class="contact"><p class="name">Tobin R. Castellan</p><p>303.555.0192</p><p>tobin.castellan@alderpine.example</p></div>
        <div class="contact"><p class="name">Idris Vantelle</p><p>303.555.0176</p><p>idris.vantelle@alderpine.example</p></div>
        <div class="contact"><p class="name">Leona Marchetti</p><p>leona@alderpine.example</p></div>
        <div class="contact"><p class="name">Ferris Oakhurst</p><p>48 Lindel Rd</p><p>Springfield, USA</p><p>414-555-0171</p><p>ferris@quabbleton.example</p></div>
        <div class="brand"><span class="dot"></span>Alderpine</div>
      </div>
    </section>

    <section class="page page-front">
      <div class="front-photo" role="img" aria-label="Fog drifting over a row of pine treetops"></div>
      <div class="web-tag">www.alderpine.example</div>
      <div class="mist-panel"></div>
      <div class="title-panel">
        <p class="kicker">WE MAKE THE</p>
        <h1 class="headline">COMPLEX<br>SIMPLE</h1>
        <p class="lede">Most people share a central fear; that at some point in their lives, they will need money and not have it. Wealth is the absence of that fear.</p>
      </div>
      <div class="brand"><span class="dot"></span>Alderpine</div>
    </section>
  </main>
</body>
</html>
```